Corvath Properties Business Card Design

We would now like to design business cards with the new Corvath Properties logo

Target Market(s)

Professional

Industry/Entity Type

Professional services

Contact Information for Business Card

Employee name, title, phone number, email address, corporate office address and logo.

Font styles to use
Sans Serif

Colors
0054AA
0677BA
7BADD7
CADEEF
E8F1F8

Requirements
Must have
• My logo
Should not have
• any other pictures or images besides my logo

```html
<!DOCTYPE html>
<html lang="en">
<head>
<meta charset="UTF-8">
<title>Corvath Properties Business Card</title>
<link rel="stylesheet" href="https://fonts.googleapis.com/css2?family=Montserrat:wght@400;500;700&display=swap">
<style>
  :root {
    --brand-blue: #0677BA;
    --brand-deep: #0054AA;
    --brand-sky: #7BADD7;
    --brand-mist: #CADEEF;
    --brand-ice: #E8F1F8;
    --card-paper: #EEF0F2;
    --backdrop: #D9DCE0;
  }
  html, body {
    margin: 0;
    padding: 0;
    width: 1200px;
    height: 840px;
    overflow: hidden;
    background: var(--backdrop);
    font-family: "Montserrat", sans-serif;
  }
  .canvas {
    width: 1200px;
    height: 840px;
    display: flex;
    flex-direction: column;
    align-items: center;
    justify-content: center;
    gap: 40px;
  }
  .card {
    width: 630px;
    height: 360px;
    border-radius: 26px;
    position: relative;
    overflow: hidden;
    box-sizing: border-box;
  }
  /* Back side */
  .card-back {
    background: var(--brand-blue);
    display: flex;
    align-items: center;
    justify-content: center;
    gap: 18px;
  }
  .card-back .brand-name {
    color: var(--brand-ice);
    font-weight: 700;
    font-size: 40px;
    letter-spacing: 0.5px;
  }
  .card-back .brand-square {
    width: 34px;
    height: 34px;
    background: var(--brand-ice);
  }
  /* Front side */
  .card-front {
    background: var(--card-paper);
  }
  .brand-panel {
    position: absolute;
    left: 0;
    top: 0;
    width: 260px;
    height: 100%;
    display: flex;
    flex-direction: column;
    align-items: flex-start;
    justify-content: center;
    padding-left: 40px;
    box-sizing: border-box;
    gap: 16px;
  }
  .brand-panel .brand-square {
    width: 30px;
    height: 30px;
    background: var(--brand-blue);
  }
  .brand-panel .brand-name {
    color: var(--brand-blue);
    font-weight: 700;
    font-size: 30px;
    line-height: 1.1;
  }
  .identity {
    position: absolute;
    right: 58px;
    top: 44px;
    display: flex;
    align-items: center;
    color: var(--brand-blue);
  }
  .identity .person-name {
    font-weight: 700;
    font-size: 25px;
  }
  .identity .divider {
    width: 2px;
    height: 28px;
    background: var(--brand-blue);
    margin: 0 16px;
  }
  .identity .person-title {
    font-weight: 400;
    font-size: 12px;
    letter-spacing: 1px;
  }
  .contact-list {
    position: absolute;
    left: 330px;
    top: 168px;
    margin: 0;
    padding: 0;
    list-style: none;
    color: var(--brand-blue);
    font-size: 15px;
    font-weight: 500;
  }
  .contact-list li {
    display: flex;
    align-items: center;
    gap: 16px;
    height: 34px;
  }
  .contact-list svg {
    width: 18px;
    height: 18px;
    fill: var(--brand-blue);
    flex: none;
  }
</style>
</head>
<body>
  <main class="canvas">
    <section class="card card-back" aria-label="Card back">
      <span class="brand-square"></span>
      <span class="brand-name">Corvath Properties</span>
    </section>

    <section class="card card-front" aria-label="Card front">
      <div class="brand-panel">
        <span class="brand-square"></span>
        <span class="brand-name">Corvath<br>Properties</span>
      </div>

      <header class="identity">
        <span class="person-name">Your Name</span>
        <span class="divider"></span>
        <span class="person-title">TITLE</span>
      </header>

      <ul class="contact-list">
        <li>
          <svg viewBox="0 0 24 24" aria-hidden="true"><path d="M12 2a7 7 0 0 0-7 7c0 5.2 7 13 7 13s7-7.8 7-13a7 7 0 0 0-7-7zm0 9.5A2.5 2.5 0 1 1 12 6.5a2.5 2.5 0 0 1 0 5z"/></svg>
          <span>ADDRESS - xxxxxxxxxxx</span>
        </li>
        <li>
          <svg viewBox="0 0 24 24" aria-hidden="true"><path d="M6.6 10.8a15.1 15.1 0 0 0 6.6 6.6l2.2-2.2a1 1 0 0 1 1-.25 11.4 11.4 0 0 0 3.6.57 1 1 0 0 1 1 1V20a1 1 0 0 1-1 1A17 17 0 0 1 3 4a1 1 0 0 1 1-1h3.5a1 1 0 0 1 1 1c0 1.25.2 2.45.57 3.57a1 1 0 0 1-.25 1z"/></svg>
          <span>PHONE - xxxxxxxxxxx</span>
        </li>
        <li>
          <svg viewBox="0 0 24 24" aria-hidden="true"><path d="M3 5h18a1 1 0 0 1 1 1v12a1 1 0 0 1-1 1H3a1 1 0 0 1-1-1V6a1 1 0 0 1 1-1zm1.4 2 7.6 6 7.6-6zM4 9v8h16V9l-8 6.3z"/></svg>
          <span>E-MAIL - xxxxxxxxxxx</span>
        </li>
      </ul>
    </section>
  </main>
</body>
</html>
```